Harrow Bend Family Law magazine ad

I need an ad that will run in Marlow Creek Living Magazine here in NC. The ad will be a 1/2 page ad, (7.25X4.875). Resolution is 300 dpi or higher.

We are a family law firm (divorce) and we want to high light child custody issues. I would like the ad copy to include our logo (which you can find on our website www.harrowbendfamilylaw.com) and I can send a high res one if you are chosen. Ad MUST include our address and phone number by state law.

Ad copy will be something about protecting children (something brief) like "Protect what you love" or something like that. I will pick quick as I have to turn it in on Wednesday. You will need to be able to email the final product to graphics@marlowcreeklivingmag.com and me too.

Target Market(s)

Married couples with kids (primarily men) ages 35-50

Industry/Entity Type

Legal

Colors
85cae6
cadf82
fbee3f
fbf289
33a6d7
33b8a4
add136

Requirements
Must have
• website, logo, address, and phone number
Nice to have
• creative and heart provoking (I want the image to make me want to act)
Should not have
• Don't be boring or give me some stock photo I have seen in a million divorce ads.

```html
<!DOCTYPE html>
<html lang="en">
<head>
<meta charset="utf-8">
<title>Harrow Bend Family Law – Magazine Ad</title>
<link href="https://fonts.googleapis.com/css2?family=Quicksand:wght@300;400;500&display=swap" rel="stylesheet">
<style>
  :root {
    --page: #ffffff;
    --panel: #f2f3f2;
    --ink: #58595b;
    --rule: #6d6e70;
    --leaf: #a8d273;
    --brand: #33a6d7;
    --brand-ring: #add136;
  }
  * { margin: 0; padding: 0; box-sizing: border-box; }
  html, body {
    width: 1200px; height: 807px; overflow: hidden;
    background: var(--page);
    font-family: "Quicksand", sans-serif;
    color: var(--ink);
  }
  .ad {
    position: absolute; left: 15px; top: 15px;
    width: 1170px; height: 776px;
    background: var(--panel);
  }
  .kicker {
    position: absolute; right: 765px; top: 258px;
    text-align: right; font-size: 26px; font-weight: 400;
    line-height: 27.5px; letter-spacing: 0.2px; text-transform: uppercase;
  }
  .divider {
    position: absolute; left: 427px; top: 247px;
    width: 1.5px; height: 110px; background: var(--rule);
  }
  .headline {
    position: absolute; left: 436px; top: 226px;
    font-size: 146px; font-weight: 300; line-height: 1;
    color: var(--leaf); letter-spacing: -2px; white-space: nowrap;
  }
  .cta {
    position: absolute; right: 186px; top: 383px; text-align: right;
  }
  .cta-line { font-size: 21px; font-weight: 400; line-height: 28px; }
  .cta-phone { font-size: 27px; font-weight: 400; line-height: 36px; }
  .brand {
    position: absolute; right: 58px; top: 597px;
    display: flex; align-items: center; gap: 10px;
  }
  .brand-mark { width: 34px; height: 34px; }
  .brand-name {
    font-size: 21px; font-weight: 500; color: var(--brand); white-space: nowrap;
  }
  .contact {
    position: absolute; right: 58px; top: 665px;
    text-align: right; font-size: 11.5px; line-height: 13.8px; font-weight: 500;
    color: var(--ink);
  }
</style>
</head>
<body>
  <main class="ad">
    <p class="kicker">Your child<br>did not file<br>for divorce.</p>
    <div class="divider"></div>
    <h1 class="headline">YOU DID.</h1>
    <div class="cta">
      <p class="cta-line">Discuss your child’s protection with us.</p>
      <p class="cta-phone">Call 910-555-0172</p>
    </div>
    <div class="brand">
      <svg class="brand-mark" viewBox="0 0 34 34" aria-hidden="true">
        <circle cx="17" cy="17" r="15" fill="none" stroke="var(--brand-ring)" stroke-width="3"/>
      </svg>
      <span class="brand-name">Harrow Bend Family Law</span>
    </div>
    <address class="contact" style="font-style:normal">
      1420 Linden Court, Suite 210, Wilmington, NC 28403<br>
      Email: mara@harrowbendfamilylaw.com<br>
      Phone: 910-555-0172<br>
      Fax: 877-555-0139<br>
      Web: www.harrowbendfamilylaw.com
    </address>
  </main>
</body>
</html>
```